Business Cards

I am a landscape designer and I am hired to do over the top landscapes!
I pay attention to detail and do everything from growing my own orchids and Fruits and Vegetables.
I build ponds water features. I do Landscape Lighting and Specialize in Drip Irrigation for New Landscapes.
I am looking for something with a picture of one of my landscapes and pictures of Orchids on the back so I can work on growing my Orchid business.
I like the plastic cards.
I like Saturation
I like color and I want something that really sticks out!
I will attach a few pics!
Thanks
Corey
A Bright Terrace LLC
Corey Valdrup
Orchids & Organic Farming
Landscaping Made Bright
555-204-7193
Abrightterrace@mailnest.example
Sandpiper Cove FL

Target Market(s)

I work for Wealthy Clients who want unique designs and enjoy rare plants.
I am the goto guy for tropical and rare plants
Cool Designs
Orchids
Interior Decorating
Exterior Lighting
Organic Farming
People who appreciate plants

Industry/Entity Type

Landscape

Font styles to use
Decorative

Requirements
Must have
• COLOR COLOR COLOR
Saturation
Sleek and Clean
Should not have
• tacky

```html
<!DOCTYPE html>
<html lang="en">
<head>
<meta charset="utf-8">
<title>A Bright Terrace – Business Card</title>
<link rel="stylesheet" href="https://fonts.googleapis.com/css2?family=Cinzel+Decorative:wght@400;700&family=Cinzel:wght@400;600;700&display=swap">
<style>
  :root {
    --page: #ffffff;
    --forest: #22362e;
    --lime: #16d416;
    --moss: #2f5a35;
    --ink: #ffffff;
    --violet: #4a1878;
    --orchid: #8a2be2;
    --orchid-deep: #5b12a8;
    --outline:
      -2px -2px 0 var(--violet), 2px -2px 0 var(--violet),
      -2px 2px 0 var(--violet), 2px 2px 0 var(--violet),
      0 -2px 0 var(--violet), 0 2px 0 var(--violet),
      -2px 0 0 var(--violet), 2px 0 0 var(--violet);
  }
  * { box-sizing: border-box; margin: 0; padding: 0; }
  html, body {
    width: 1200px; height: 1000px; overflow: hidden;
    background: var(--page);
  }
  .canvas { position: relative; width: 1200px; height: 1000px; }

  /* Front card */
  .card-front {
    position: absolute; left: 193px; top: 5px; width: 814px; height: 486px;
  }
  .brand-bar {
    height: 142px; background: var(--forest);
    display: flex; flex-direction: column; align-items: center; justify-content: center;
  }
  .brand-name {
    font-family: "Cinzel Decorative", "Cinzel", serif;
    font-weight: 700; font-size: 54px; line-height: 54px;
    color: var(--ink); text-align: center;
  }
  .gallery {
    display: flex; gap: 2px; height: 267px; margin-top: 1px; background: #fff;
  }
  .gallery .shot { flex: 1; }
  .shot--palm { background: linear-gradient(160deg, #c34a2b 0%, #3c8d2e 45%, #1f5c23 100%); }
  .shot--gerbera { background: radial-gradient(circle at 45% 60%, #f0844e 0%, #e9a0a8 30%, #3d6b22 70%, #6e3a1c 100%); }
  .shot--salvia { background: linear-gradient(170deg, #3f7a2a 0%, #d9332a 35%, #6a4ad0 75%, #2f5d23 100%); }
  .shot--rockbed { background: linear-gradient(150deg, #2e8a3c 0%, #56b24a 45%, #b5a78c 80%, #6b6b6b 100%); }
  .tagline-band {
    height: 74px; margin-top: 2px;
    background: linear-gradient(90deg, var(--lime) 0%, #17c517 45%, var(--moss) 100%);
    display: flex; align-items: center; justify-content: center;
  }
  .tagline {
    font-family: "Cinzel", serif; font-weight: 700; font-size: 42px;
    color: var(--ink); text-shadow: var(--outline); letter-spacing: 0.5px;
    white-space: nowrap;
  }

  /* Back card */
  .card-back {
    position: absolute; left: 191px; top: 500px; width: 816px; height: 488px;
  }
  .contact-panel {
    height: 241px; background: var(--forest); padding: 20px 0 0 24px;
  }
  .owner-name {
    font-family: "Cinzel Decorative", serif; font-weight: 700;
    font-size: 54px; line-height: 64px;
    color: var(--ink); text-shadow: var(--outline); white-space: nowrap;
  }
  .contact-line {
    font-family: "Cinzel", serif; font-weight: 600;
    font-size: 30px; line-height: 39px;
    color: var(--ink); text-shadow: var(--outline); white-space: nowrap;
  }
  .contact-line--email { font-size: 27px; }
  .services-panel {
    position: relative; height: 247px;
    background: linear-gradient(90deg, var(--lime) 0%, #17c517 45%, var(--moss) 100%);
  }
  .orchid-art {
    position: absolute; left: 40px; top: -16px; width: 360px; height: 262px;
    border-radius: 48% 52% 45% 55%;
    background: radial-gradient(ellipse at 45% 45%, var(--orchid) 0%, var(--orchid-deep) 55%, rgba(91,18,168,0) 75%);
  }
  .service-list {
    position: absolute; right: 28px; top: 14px; list-style: none; text-align: right;
  }
  .service-list li {
    font-family: "Cinzel", serif; font-weight: 600;
    font-size: 32px; line-height: 36px; letter-spacing: 0.5px;
    color: var(--ink); text-shadow: var(--outline); white-space: nowrap;
  }
</style>
</head>
<body>
<main class="canvas">
  <section class="card-front">
    <header class="brand-bar">
      <div class="brand-name">A Bright</div>
      <div class="brand-name">Terrace</div>
    </header>
    <div class="gallery">
      <div class="shot shot--palm" role="img" aria-label="Photo of a tropical garden bed with palm and colorful foliage"></div>
      <div class="shot shot--gerbera" role="img" aria-label="Photo of gerbera daisies and impatiens around a tree trunk"></div>
      <div class="shot shot--salvia" role="img" aria-label="Photo of a flower bed with red and purple salvia"></div>
      <div class="shot shot--rockbed" role="img" aria-label="Photo of a landscaped bed with ferns, bromeliads and river rock"></div>
    </div>
    <div class="tagline-band">
      <p class="tagline">Landscaping Made Bright</p>
    </div>
  </section>

  <section class="card-back">
    <div class="contact-panel">
      <h1 class="owner-name">Corey Valdrup</h1>
      <p class="contact-line">555-204-7193</p>
      <p class="contact-line contact-line--email">Abrightterrace@mailnest.example</p>
      <p class="contact-line">Sandpiper Cove FL</p>
    </div>
    <div class="services-panel">
      <div class="orchid-art" role="img" aria-label="Photo of a purple vanda orchid spray"></div>
      <ul class="service-list">
        <li>Landscaping</li>
        <li>Organic Farming</li>
        <li>Orchids</li>
        <li>Tropical Plants</li>
        <li>Rare Plants</li>
        <li>Exterior Lighting</li>
      </ul>
    </div>
  </section>
</main>
</body>
</html>
```